University Student Business Card

Looking for a professional university student business card. Student is studying business with a focus on marketing. Some combination using a monogram and/or full name on the front with full name, university details and contact information on the back. Card should be modern design for a young professional. Prefer use of royal blue, black and white but am open to other uses of colour palette if it reinforces young/trendy style. Initials for a monogram are: KM. Full details will be provided in private consultation with designer(s).

Target Market(s)

Professional business people, marketers, advertisers, consultants

Industry/Entity Type

Business, marketing

Contact Information for Business Card

Monogram or personal logo, full name, university name, program of study, phone number, email address, kaimorrow.link address

Other font styles liked:
• Open to suggestion to fulfill above requirements

Colors
0054AA
0677BA
7BADD7
CADEEF
E8F1F8

Requirements
Must have
• Monogram using letters K and M, and incorporate the business card details listed in the brief (specific details including personal contact info will be shared with successful designer to ensure privacy)
Nice to have
• Personal brand using monogram or personal logo (not a business logo)

```html
<!DOCTYPE html>
<html lang="en">
<head>
<meta charset="UTF-8">
<title>Kai Morrow – Student Business Card</title>
<link href="https://fonts.googleapis.com/css2?family=Lato:wght@400;700&display=swap" rel="stylesheet">
<style>
  :root {
    --backdrop: #e4e5e6;
    --card-dark: #12121c;
    --card-mid: #23232f;
    --royal: #34357f;
    --royal-soft: #2f3070;
    --ink-light: #f2f2f6;
    --rule: #3a3b80;
  }
  * { margin: 0; padding: 0; box-sizing: border-box; }
  html, body {
    width: 1200px; height: 800px; overflow: hidden;
    background: var(--backdrop);
    font-family: "Lato", Arial, sans-serif;
  }
  .canvas {
    width: 1200px; height: 800px;
    display: flex; align-items: center; justify-content: center; gap: 44px;
  }
  .card {
    position: relative;
    width: 520px; height: 300px;
    border-radius: 18px;
    background: linear-gradient(120deg, var(--card-mid) 0%, var(--card-dark) 70%);
    overflow: hidden;
  }
  /* Information side */
  .card--info .identity {
    position: absolute; right: 286px; top: 128px;
    text-align: right;
  }
  .identity__name {
    color: var(--royal);
    font-weight: 700; font-size: 25px; letter-spacing: 0.5px;
    line-height: 1;
  }
  .identity__program {
    color: var(--ink-light);
    font-size: 16px; margin-top: 4px;
  }
  .card--info .divider {
    position: absolute; left: 252px; top: 86px;
    width: 1.5px; height: 128px; background: var(--rule);
  }
  .details {
    position: absolute; left: 274px; top: 92px;
    color: var(--ink-light); font-size: 15px; line-height: 1.15;
  }
  .details__school { margin-bottom: 12px; }
  .details__school span { display: block; }
  .details__school .address { padding-left: 16px; }
  .contact-list { list-style: none; }
  .contact-list li {
    display: flex; align-items: center; gap: 7px;
    font-size: 15.5px; line-height: 1.2;
  }
  .contact-list svg { width: 11px; height: 11px; flex: none; }
  /* Monogram side */
  .card--mark .monogram {
    position: absolute; left: 0; right: 0; top: 50%;
    transform: translateY(-50%);
    text-align: center;
    color: var(--royal);
    font-weight: 400; font-size: 150px; letter-spacing: 6px;
    line-height: 1;
  }
</style>
</head>
<body>
<main class="canvas">
  <section class="card card--info">
    <div class="identity">
      <p class="identity__name">KAI MORROW</p>
      <p class="identity__program">program of study</p>
    </div>
    <div class="divider"></div>
    <div class="details">
      <p class="details__school">
        <span>University Name</span>
        <span class="address">address here</span>
      </p>
      <ul class="contact-list">
        <li>
          <svg viewBox="0 0 12 12" aria-hidden="true"><path d="M2.5 1 L4.5 1 L5 3.5 L3.8 4.4 C4.5 6 6 7.5 7.6 8.2 L8.5 7 L11 7.5 L11 9.5 C11 10.4 10.3 11 9.5 11 C5 10.6 1.4 7 1 2.5 C1 1.7 1.6 1 2.5 1 Z" fill="#3a3b80"/></svg>
          123-456-7890
        </li>
        <li>
          <svg viewBox="0 0 12 12" aria-hidden="true"><rect x="1" y="2.5" width="10" height="7" fill="#3a3b80"/><path d="M1 2.5 L6 6.5 L11 2.5" stroke="#12121c" stroke-width="1" fill="none"/></svg>
          youremail@email.com
        </li>
        <li>
          <svg viewBox="0 0 12 12" aria-hidden="true"><circle cx="6" cy="6" r="5" fill="#3a3b80"/></svg>
          kaimorrow.link
        </li>
      </ul>
    </div>
  </section>

  <section class="card card--mark">
    <p class="monogram">KM</p>
  </section>
</main>
</body>
</html>
```